Vantor Medica Innovative Business Card

Stunning business card. Background will be black. Letters in gold. Modern yet simple design that is attention grabbing. QR code leading to site. Attractive primarily to males ages 30 to 50 but also to females in same age range looking for beauty and mental health products

Target Market(s)

Males in the 30-50 age demographics

Industry/Entity Type

Pharmaceuticals selling erectile dysfunction and mens health medications

Contact Information for Business Card

www.vantormedica.example; (775) BUY-KELO; info@vantormedica.example

Colors
FFC000
F8CF3A
FAE287
FDF2CF
FEFAEE

Requirements
Must have
• Black business card with gold letters.
Nice to have
• perhaps just the logo or the "R" icon by itself on one side
Should not have
• too much content so it does not look busy

```html
<!DOCTYPE html>
<html lang="en">
<head>
<meta charset="utf-8">
<title>Vantor Medica Business Card</title>
<link rel="stylesheet" href="https://fonts.googleapis.com/css2?family=Nunito:wght@400;800&display=swap">
<style>
  :root {
    --page: #141314;
    --card-top: #2d292a;
    --card-bottom: #1c1a1b;
    --gold: #e9c545;
    --gold-deep: #d9ad2c;
    --ink-light: #f2f0ee;
    --pattern-a: #3a3738;
    --pattern-b: #232122;
  }
  * { margin: 0; padding: 0; box-sizing: border-box; }
  html, body { width: 1200px; height: 1200px; overflow: hidden; }
  body {
    background: var(--page);
    display: flex;
    flex-direction: column;
    align-items: center;
    justify-content: center;
    gap: 56px;
    font-family: "Nunito", sans-serif;
  }
  .card {
    position: relative;
    width: 820px;
    height: 469px;
    border-radius: 6px;
    background: linear-gradient(160deg, var(--card-top), var(--card-bottom));
    box-shadow: 0 18px 40px rgba(0,0,0,.55);
    overflow: hidden;
  }
  .card-back .pattern {
    position: absolute;
    inset: 0;
    background: radial-gradient(circle at 50% 45%, var(--pattern-a), var(--pattern-b) 75%);
  }
  .brand {
    display: flex;
    align-items: center;
    gap: 14px;
    color: var(--gold);
    font-weight: 800;
    letter-spacing: 0.04em;
    text-transform: uppercase;
    white-space: nowrap;
  }
  .brand-dot {
    width: 22px; height: 22px;
    border-radius: 50%;
    background: var(--gold);
    flex: none;
  }
  .card-back .brand {
    position: absolute;
    left: 50%; top: 50%;
    transform: translate(-50%, -50%);
    font-size: 46px;
  }
  .card-front .brand {
    position: absolute;
    right: 80px; top: 120px;
    font-size: 40px;
  }
  .contacts {
    position: absolute;
    left: 70px; top: 190px;
    list-style: none;
    color: var(--ink-light);
    font-size: 19px;
    line-height: 1.75;
  }
  .contacts li { display: flex; align-items: center; gap: 12px; }
  .contacts svg { width: 16px; height: 16px; fill: var(--gold); flex: none; }
  .person {
    position: absolute;
    right: 110px; bottom: 70px;
    text-align: right;
  }
  .person-name {
    color: var(--gold);
    font-weight: 800;
    font-size: 36px;
    line-height: 1.15;
  }
  .person-role {
    color: var(--ink-light);
    font-size: 22px;
    margin-top: 4px;
  }
  .edge-tab {
    position: absolute;
    right: 0; bottom: 0;
    width: 60px; height: 34px;
    border-radius: 10px 0 0 0;
    background: var(--gold-deep);
  }
</style>
</head>
<body>
  <section class="card card-back">
    <div class="pattern" role="img" aria-label="Repeating embossed brand monogram pattern in dark grey"></div>
    <div class="brand"><span class="brand-dot"></span>Vantor Medica</div>
  </section>

  <section class="card card-front">
    <ul class="contacts">
      <li>
        <svg viewBox="0 0 16 16" aria-hidden="true"><path d="M3.6 1.2 6 3.6 4.7 5.5c.9 2 2.4 3.6 4.5 4.6l1.9-1.3 2.4 2.4-1.6 2.6C6.5 13.6 1.9 9 1.2 2.8z"/></svg>
        (775)-555-014
      </li>
      <li>
        <svg viewBox="0 0 16 16" aria-hidden="true"><path d="M1 3h14v10H1z M1.8 3.8 8 8.6l6.2-4.8" /></svg>
        info@vantormedica.example
      </li>
      <li>
        <svg viewBox="0 0 16 16" aria-hidden="true"><circle cx="8" cy="8" r="7"/></svg>
        www.vantormedica.example
      </li>
    </ul>
    <div class="brand"><span class="brand-dot"></span>Vantor Medica</div>
    <div class="person">
      <p class="person-name">Marlow Tenn</p>
      <p class="person-role">Founder &amp; Director</p>
    </div>
    <div class="edge-tab"></div>
  </section>
</body>
</html>
```